Movie poster for short film: TINFOIL

We need a creative, artistic, stylized poster design for our short film TINFOIL. We would like to see designs with graphics and bold colors more than photographs. The photographs we are posting are more for reference- you do not have to use them in the poster! We are looking for something clean and simple. The film is a drama so please don't make it funny. The mood of the film is thoughtful and introspective. Name of film should be in all caps. Things to include in the poster:
Name of film: TINFOIL
Velvet Harbor Pictures
Starring Marisa Calloway

Here is a brief plot synopsis: TINFOIL follows one night in the life of a rebellious young woman who breaks into a diner after hours with a can of spray paint. Her intentions change after she ends up discovering what's left of a love story.

The movie is somewhat experimental, set to music for part of it with no dialog. The whole movie takes place in an old fashioned diner.

Target Market(s)

Film festival attendees between the ages of 20-50

Industry/Entity Type

Movie

Font styles to use
Sans Serif

Requirements
Must have
• See project description above- also the film is somewhat dark in nature so please don't make it too 'happy' looking.

```html
<!DOCTYPE html>
<html lang="en">
<head>
<meta charset="utf-8">
<title>Tinfoil — Poster</title>
<link rel="stylesheet" href="https://fonts.googleapis.com/css2?family=Pacifico&family=Oswald:wght@300;400;600&display=swap">
<style>
  :root {
    --stage: #333333;
    --paper: #efeeeb;
    --shadow-band: #dfdedb;
    --title-red: #a8232c;
    --ink: #151515;
    --machine-red: #b8272e;
    --machine-glass: #e6e5e2;
    --badge: #2a2a2a;
  }
  html, body {
    margin: 0;
    padding: 0;
    width: 1200px;
    height: 900px;
    overflow: hidden;
    background: var(--stage);
  }
  .poster {
    position: absolute;
    left: 314px;
    top: 13px;
    width: 572px;
    height: 868px;
    background: var(--paper);
    overflow: hidden;
  }
  .long-shadow {
    position: absolute;
    left: 0;
    top: 0;
  }
  .hero-illustration {
    position: absolute;
    left: 177px;
    top: 137px;
    width: 218px;
    height: 343px;
    border-radius: 6px;
    background: linear-gradient(180deg, var(--machine-glass) 0%, var(--machine-glass) 52%, var(--machine-red) 62%, #7a1317 100%);
  }
  .film-title {
    position: absolute;
    left: 0;
    width: 100%;
    top: 530px;
    margin: 0;
    text-align: center;
    font-family: 'Oswald', sans-serif;
    font-weight: 600;
    font-size: 122px;
    line-height: 140px;
    letter-spacing: 8px;
    text-indent: 8px;
    text-transform: uppercase;
    color: var(--title-red);
  }
  .credits {
    position: absolute;
    left: 0;
    width: 100%;
    top: 710px;
    text-align: center;
    color: var(--ink);
  }
  .studio {
    margin: 0;
    font-family: 'Pacifico', cursive;
    font-size: 30px;
    line-height: 44px;
    letter-spacing: 0.5px;
  }
  .presents {
    margin: -4px 0 0;
    font-family: 'Oswald', sans-serif;
    font-weight: 300;
    font-size: 14px;
    line-height: 20px;
  }
  .billing {
    margin: 6px 0 0;
    font-family: 'Oswald', sans-serif;
    font-weight: 300;
    font-size: 28px;
    line-height: 38px;
    letter-spacing: -0.5px;
  }
  .billing .starring {
    font-size: 11px;
    margin: 0 3px;
  }
  .fine-print {
    display: flex;
    justify-content: center;
    align-items: center;
    gap: 12px;
    margin-top: 8px;
    font-family: 'Oswald', sans-serif;
    font-weight: 300;
    font-size: 8px;
  }
  .web { margin-right: 10px; }
  .badge {
    display: inline-block;
    height: 14px;
    background: var(--badge);
  }
  .badge.rating { width: 30px; }
  .badge.sound { width: 26px; }
  .badge.audio { width: 30px; }
</style>
</head>
<body>
  <main class="poster">
    <svg class="long-shadow" width="572" height="868" viewBox="0 0 572 868" aria-hidden="true">
      <polygon fill="var(--shadow-band)" points="395,161 572,338 572,868 565,868 177,480 395,480"/>
    </svg>

    <div class="hero-illustration" role="img" aria-label="Flat illustration of a red gumball machine filled with colourful gumballs"></div>

    <h1 class="film-title">Tinfoil</h1>

    <section class="credits">
      <p class="studio">Velvet Harbor Pictures</p>
      <p class="presents">presents</p>
      <p class="billing">Tinfoil<span class="starring">starring</span>Marisa Calloway</p>
      <div class="fine-print">
        <span class="web">www.velvetharborpictures.com/films</span>
        <span class="badge rating"></span>
        <span class="badge sound"></span>
        <span class="badge audio"></span>
      </div>
    </section>
  </main>
</body>
</html>
```